Fitness Body Weight Exercises Book Cover

Need a book cover design for a new book

This book is going to market to people to get in shape by playing a fitness dice game call FlexTRIO The dice game

When people see the cover they should see that this is a book that can help them get in shape. We are positioning the guru as an expert inside of the fitness niche

Target Market(s)

fitness

Requirements
Must have
• The name of the book which is

"The Grand Summit Frame Regimen"

Tagline -

The Worlds #1 Resource For Combat Strength Training Using Body Weight Exercises For Men, Women and Children

__________

Featuring FlexTRIO The Dice Game (TM)

___________________________
ON THE BACK COVER

Image with Oren with his gold medal
with these words
No Weights, No Problem

_____-

front cover
the image with him doing a push up should be on the front of the cover with these words

_________
Nice to have
• Maybe

"Oren Presents ...."

The Grand Summit Frame Regimen

```html
<!DOCTYPE html>
<html lang="en">
<head>
<meta charset="utf-8">
<title>The Grand Summit Frame Regimen — Front and Back Cover</title>
<link href="https://fonts.googleapis.com/css2?family=Michroma&family=Teko:wght@300;400;600;700&display=swap" rel="stylesheet">
<style>
  :root {
    --ink: #050505;
    --cover: #0b0b0b;
    --cover-top: #2e2e2e;
    --frame: #5a5a5a;
    --white: #ffffff;
    --yellow: #f2e630;
    --lime: #c9e35a;
    --green: #7bd36a;
    --teal: #4fe8c0;
    --cyan: #2cf5ff;
    --orange: #f0a040;
    --red: #e0442a;
    --tag-text: #e8e8e8;
  }
  * { margin: 0; padding: 0; box-sizing: border-box; }
  html, body { width: 1200px; height: 800px; overflow: hidden; background: var(--ink); }
  .spread { position: relative; width: 1200px; height: 800px; background: var(--ink); overflow: hidden; }

  .accent-band { position: absolute; inset: 0; width: 1200px; height: 800px; }

  .side-label {
    position: absolute; top: 74px;
    font-family: "Michroma", sans-serif; font-size: 44px; line-height: 1;
    color: var(--white); letter-spacing: -1px; transform: scaleX(1.12); transform-origin: left top;
  }
  .side-label--front { left: 41px; }
  .side-label--back { left: 740px; }

  .cover {
    position: absolute; top: 137px; width: 418px; height: 627px;
    border: 1px solid var(--frame);
    background: linear-gradient(180deg, var(--cover-top) 0%, #151515 9%, var(--cover) 20%, var(--cover) 100%);
    overflow: hidden;
  }
  .cover--front { left: 42px; }
  .cover--back { left: 741px; }

  .chevron { position: absolute; left: 0; top: 0; width: 70px; height: 72px; }

  .title { position: absolute; left: 0; top: 0; width: 100%; height: 100%; font-family: "Teko", sans-serif; font-weight: 700; text-transform: uppercase; }
  .title-line { position: absolute; line-height: 1; transform: skewX(-10deg); white-space: nowrap; letter-spacing: 1px; }
  .title-line--lead { left: 58px; top: 34px; font-size: 50px; color: var(--white);
    background: linear-gradient(180deg, #ffffff 40%, #9a9a9a); -webkit-background-clip: text; background-clip: text; -webkit-text-fill-color: transparent; }
  .title-line--hot { left: 168px; top: 66px; font-size: 58px;
    background: linear-gradient(90deg, var(--yellow), var(--orange) 50%, var(--red)); -webkit-background-clip: text; background-clip: text; -webkit-text-fill-color: transparent; }
  .title-line--cool { left: 58px; top: 104px; font-size: 62px;
    background: linear-gradient(90deg, var(--yellow), var(--green) 50%, var(--teal)); -webkit-background-clip: text; background-clip: text; -webkit-text-fill-color: transparent; }
  .title-line--tail { left: 208px; top: 142px; font-size: 56px;
    background: linear-gradient(180deg, #ffffff 40%, #9a9a9a); -webkit-background-clip: text; background-clip: text; -webkit-text-fill-color: transparent; }

  .photo { position: absolute; }
  .photo--pushup { left: 0; top: 280px; width: 418px; height: 347px;
    background: radial-gradient(ellipse 60% 55% at 62% 55%, #6d6d6d 0%, #3a3a3a 45%, rgba(11,11,11,0) 80%); }
  .photo--medal { left: 70px; top: 258px; width: 300px; height: 369px;
    background:
      radial-gradient(ellipse 40% 60% at 42% 78%, rgba(95,150,60,0.85) 0%, rgba(60,100,40,0.5) 50%, rgba(11,11,11,0) 85%),
      radial-gradient(ellipse 45% 55% at 55% 50%, #5a5a5a 0%, #2a2a2a 55%, rgba(11,11,11,0) 85%); }

  .tagline { position: absolute; left: 21px; bottom: 20px; padding-left: 12px; border-left: 4px solid var(--yellow);
    font-family: "Teko", sans-serif; font-weight: 300; font-size: 16.5px; line-height: 16px; color: var(--tag-text); text-transform: uppercase; }
  .tagline-rank { font-size: 22px; font-weight: 400; color: var(--yellow); }

  .back-headline { position: absolute; left: 118px; top: 122px;
    font-family: "Teko", sans-serif; font-weight: 300; font-size: 58px; line-height: 54px; letter-spacing: 1px;
    background: linear-gradient(180deg, #ffffff 45%, #8d8d8d); -webkit-background-clip: text; background-clip: text; -webkit-text-fill-color: transparent; }
</style>
</head>
<body>
<main class="spread">
  <svg class="accent-band" viewBox="0 0 1200 800" aria-hidden="true">
    <defs>
      <linearGradient id="band-fade" x1="0" y1="0" x2="0" y2="1">
        <stop offset="0" stop-color="#d2e25a"/>
        <stop offset="0.45" stop-color="#7deab0"/>
        <stop offset="0.75" stop-color="#2cf5ff"/>
        <stop offset="1" stop-color="#2cf5ff"/>
      </linearGradient>
    </defs>
    <polygon points="666,0 738,0 525,800 452,800" fill="url(#band-fade)"/>
  </svg>

  <h2 class="side-label side-label--front">FRONT</h2>
  <h2 class="side-label side-label--back">BACK</h2>

  <section class="cover cover--front">
    <svg class="chevron" viewBox="0 0 70 72" aria-hidden="true">
      <defs>
        <linearGradient id="chevron-fade" x1="0" y1="1" x2="1" y2="0">
          <stop offset="0" stop-color="#f2e630"/>
          <stop offset="1" stop-color="#7be89a"/>
        </linearGradient>
      </defs>
      <polygon points="35,0 47,0 66,16 37,69 0,69 0,51 27,51 44,18" fill="url(#chevron-fade)"/>
    </svg>

    <div class="photo photo--pushup" role="img" aria-label="Black and white photo of the athlete doing a push-up, looking at the camera"></div>

    <h1 class="title">
      <span class="title-line title-line--lead">The Grand</span>
      <span class="title-line title-line--hot">Summit</span>
      <span class="title-line title-line--cool">Frame</span>
      <span class="title-line title-line--tail">Regimen</span>
    </h1>

    <p class="tagline">The Worlds <span class="tagline-rank">#1</span> Resource for Combat<br>Strength Training Using Body Weight Exercises<br>For Men, Women and Children</p>
  </section>

  <section class="cover cover--back">
    <div class="photo photo--medal" role="img" aria-label="Photo of the athlete smiling and wearing a gold medal, tinted green"></div>
    <p class="back-headline">NO WEIGHTS,<br>NO PROBLEM</p>
  </section>
</main>
</body>
</html>
```